Redesign Colorful Business Card

Please redesign the card attached. It is too busy. Please don't eliminate any of the words. The repetivite word "free" can be used less often.

Target Market(s)

College Students.

Contact Information for Business Card

The details listed in the attached image

Font styles to use
Sans Serif

Requirements
Must have
• A clear and simple presentation and must be attractive.

```html
<!DOCTYPE html>
<html lang="en">
<head>
<meta charset="UTF-8">
<title>StudyKeel – Free Study Tools</title>
<link rel="stylesheet" href="https://fonts.googleapis.com/css2?family=Nunito:wght@800;900&display=swap">
<style>
  :root {
    --navy: #1b4790;
    --white: #ffffff;
    --sky: #8dcdf2;
    --sky-pale: #cdeaf8;
    --ink: #1a1a1a;
  }
  * { margin: 0; padding: 0; box-sizing: border-box; }
  html, body { width: 1043px; height: 1200px; overflow: hidden; }
  body {
    background: var(--navy);
    font-family: "Nunito", "Arial Rounded MT Bold", sans-serif;
    color: var(--white);
  }
  .card { position: relative; width: 1043px; height: 1200px; background: var(--navy); }
  .timeline { position: absolute; left: 0; top: 0; }
  .benefit {
    position: absolute;
    left: 501px;
    font-weight: 800;
    font-size: 52px;
    line-height: 63px;
    letter-spacing: 0.3px;
    white-space: nowrap;
  }
  .benefit--time { top: 128px; }
  .benefit--class { top: 408px; }
  .benefit--memory { top: 716px; }
  .promo-art {
    position: absolute;
    left: 51px;
    top: 303px;
    width: 331px;
    height: 358px;
    border-radius: 24px;
    background: linear-gradient(160deg, var(--sky) 0%, var(--sky-pale) 60%, var(--white) 100%);
  }
  .promo-word {
    position: absolute;
    left: 51px;
    top: 360px;
    width: 331px;
    text-align: center;
    font-weight: 800;
    font-size: 80px;
    line-height: 100px;
    letter-spacing: 10px;
    color: var(--ink);
  }
  .brand {
    position: absolute;
    left: 180px;
    top: 968px;
    display: flex;
    align-items: center;
    gap: 40px;
  }
  .brand-dot { width: 100px; height: 100px; border-radius: 50%; background: var(--sky); }
  .brand-name {
    font-weight: 800;
    font-size: 70px;
    line-height: 1;
    color: var(--white);
    text-decoration: underline;
    text-decoration-thickness: 4px;
    text-underline-offset: 8px;
  }
</style>
</head>
<body>
<main class="card">
  <svg class="timeline" width="1043" height="1200" aria-hidden="true">
    <rect x="441" y="186" width="22" height="591" rx="4" fill="var(--white)"/>
    <rect x="445" y="186" width="14" height="591" fill="var(--navy)"/>
    <rect x="449" y="186" width="6" height="591" fill="var(--white)"/>
    <g fill="var(--sky)" stroke="var(--white)" stroke-width="5">
      <circle cx="452" cy="186" r="19"/>
      <circle cx="452" cy="482" r="19"/>
      <circle cx="452" cy="777" r="19"/>
    </g>
  </svg>

  <p class="benefit benefit--time">Cut Study Time<br>Down By Up To 50%</p>
  <p class="benefit benefit--class">Learn A Subject<br>Without Having To<br>Go To Class</p>
  <p class="benefit benefit--memory">Memorize Anything<br>Quickly</p>

  <div class="promo-art" role="img" aria-label="Illustration of a megaphone announcing a free offer in a speech card with sparkles"></div>
  <p class="promo-word">FREE</p>

  <div class="brand">
    <span class="brand-dot" aria-hidden="true"></span>
    <span class="brand-name">StudyKeel.com</span>
  </div>
</main>
</body>
</html>
```